4 x Designs Required

Hi There,
I require 4 x different designs to be made for 4 new brands of mine however they can be quite interchangeable. HR Plinkr and Marketing Plinkr can be similar just with a difference in colour. The same goes for the Bulletin brands. This means there are ultimately two designs that need perfecting.

There must be a click here CTA on the banner somewhere. :-)

I require the banners in 728x90 format and 960x90 please.

Please use strap lines on the banners such as:
Essential Whitepapers for HR Professionals
Essential Whitepapers for Marketing Professionals
Your No.1 Whitepaper Resource

The brand names:
HR Plinkr
Marketing Plinkr
HR Dispatchly
Marketing Dispatchly

Examples attached.

```html
<!DOCTYPE html>
<html lang="en">
<head>
<meta charset="utf-8">
<title>Whitepaper Banners</title>
<link href="https://fonts.googleapis.com/css2?family=Lexend:wght@300;400;700;800&display=swap" rel="stylesheet">
<style>
  :root {
    --page-bg: #ececec;
    --blue-deep: #1b0a8c;
    --blue-bright: #2f14d4;
    --blue-glow: #4a3bf0;
    --night: #080808;
    --photo-blue: #2a5d8f;
    --photo-orange: #c8600f;
    --photo-green: #1f8a5a;
    --white: #ffffff;
    --green-cta: #2dbb2d;
    --green-cta-dark: #1f9a1f;
    --red-cta: #e00000;
    --red-cta-dark: #b00000;
    --red-accent: #e01010;
  }
  * { box-sizing: border-box; margin: 0; padding: 0; }
  html, body {
    width: 1200px; height: 675px; overflow: hidden;
    background: var(--page-bg);
    font-family: "Lexend", sans-serif;
  }
  .canvas { position: relative; width: 1200px; height: 675px; }
  .banner {
    position: absolute; left: 111px; width: 976px; height: 91px;
    overflow: hidden;
  }
  .banner--blue {
    background: linear-gradient(90deg, var(--blue-bright) 0%, var(--blue-deep) 45%, var(--blue-deep) 60%, var(--blue-bright) 100%);
  }
  .banner--night { background: var(--night); }
  .banner--hr-news { top: 58px; }
  .banner--mkt-news { top: 199px; }
  .banner--hr-bulletin { top: 360px; }
  .banner--mkt-bulletin { top: 520px; }

  .glow {
    position: absolute; inset: 0;
    background: radial-gradient(ellipse 140px 60px at 8% 50%, rgba(74,59,240,.7), transparent 70%);
  }
  .photo {
    position: absolute; left: 0; top: 0; width: 230px; height: 91px;
  }
  .photo--orange {
    background: radial-gradient(circle at 50% 35%, var(--photo-orange) 0%, transparent 40%),
                linear-gradient(90deg, var(--photo-blue) 0%, #14304d 60%, var(--night) 100%);
  }
  .photo--green {
    background: radial-gradient(circle at 50% 45%, var(--photo-green) 0%, transparent 40%),
                linear-gradient(90deg, var(--photo-blue) 0%, #14304d 60%, var(--night) 100%);
  }

  .brand {
    position: absolute; color: var(--white);
    font-weight: 800; letter-spacing: -1px; line-height: 1;
    display: flex; align-items: center; white-space: nowrap;
  }
  .brand--single { top: 0; height: 91px; }
  .brand--stacked { flex-direction: column; align-items: flex-end; line-height: 0.92; }
  .brand--hr-news { left: 50px; font-size: 44px; }
  .brand--mkt-news { left: 40px; top: 9px; font-size: 38px; }
  .brand--hr-bulletin { left: 130px; font-size: 28px; }
  .brand--mkt-bulletin { left: 118px; top: 13px; font-size: 32px; }

  .divider {
    position: absolute; top: 30px; width: 1px; height: 34px;
    background: rgba(255,255,255,.35);
  }
  .slashes { position: absolute; top: 27px; }

  .tagline {
    position: absolute; top: 0; height: 91px;
    display: flex; align-items: center;
    color: var(--white); white-space: nowrap;
  }
  .tagline--blue { font-size: 21px; font-weight: 300; letter-spacing: 1.6px; }
  .tagline--night { font-size: 17px; font-weight: 400; letter-spacing: .4px; }

  .cta {
    position: absolute; top: 30px; width: 127px; height: 31px;
    border-radius: 5px; color: var(--white);
    font-size: 15px; font-weight: 800; letter-spacing: .3px;
    display: flex; align-items: center; justify-content: center;
    border: 1px solid rgba(255,255,255,.7);
  }
  .cta--green { background: linear-gradient(180deg, var(--green-cta) 0%, var(--green-cta-dark) 100%); }
  .cta--red { background: linear-gradient(180deg, var(--red-cta) 0%, var(--red-cta-dark) 100%); }
</style>
</head>
<body>
<main class="canvas">

  <section class="banner banner--blue banner--hr-news">
    <div class="glow"></div>
    <div class="brand brand--single brand--hr-news">HR Plinkr</div>
    <div class="divider" style="left:286px"></div>
    <p class="tagline tagline--blue" style="left:305px">Essential Whitepapers for Hr Professions</p>
    <a class="cta cta--green" style="left:803px">CLICK HERE</a>
  </section>

  <section class="banner banner--blue banner--mkt-news">
    <div class="glow"></div>
    <div class="brand brand--stacked brand--mkt-news"><span>Marketing</span><span>Plinkr</span></div>
    <div class="divider" style="left:307px"></div>
    <p class="tagline tagline--blue" style="left:321px">Essential Whitepapers for Hr Professions</p>
    <a class="cta cta--green" style="left:827px">CLICK HERE</a>
  </section>

  <section class="banner banner--night banner--hr-bulletin">
    <div class="photo photo--orange" role="img" aria-label="Photo of a hand holding a tablet with a glowing globe and floating app icons"></div>
    <div class="brand brand--single brand--hr-bulletin">HR Dispatchly</div>
    <svg class="slashes" style="left:348px" width="22" height="36" viewBox="0 0 22 36" aria-hidden="true">
      <line x1="9" y1="2" x2="2" y2="34" stroke="var(--red-accent)" stroke-width="2"/>
      <line x1="19" y1="2" x2="12" y2="34" stroke="var(--red-accent)" stroke-width="2"/>
    </svg>
    <p class="tagline tagline--night" style="left:379px">Essential Whitepapers for Marketing Professionals</p>
    <a class="cta cta--red" style="left:827px">CLICK HERE</a>
  </section>

  <section class="banner banner--night banner--mkt-bulletin">
    <div class="photo photo--green" role="img" aria-label="Photo of a hand holding a tablet with a glowing globe and floating app icons"></div>
    <div class="brand brand--stacked brand--mkt-bulletin"><span>Marketing</span><span>Dispatchly</span></div>
    <svg class="slashes" style="left:352px" width="22" height="36" viewBox="0 0 22 36" aria-hidden="true">
      <line x1="9" y1="2" x2="2" y2="34" stroke="var(--red-accent)" stroke-width="2"/>
      <line x1="19" y1="2" x2="12" y2="34" stroke="var(--red-accent)" stroke-width="2"/>
    </svg>
    <p class="tagline tagline--night" style="left:379px">Essential Whitepapers for Marketing Professionals</p>
    <a class="cta cta--red" style="left:827px">CLICK HERE</a>
  </section>

</main>
</body>
</html>
```